New Board Game - TRY 45:35:20

The project is in two phases:
A. GAME BOARD DESIGN
Design of a striking game board.
NB. See the following files:
* TRY 45:35:20 Background Info
* TRY 45:35:20 Game Board Format
NB. The contest fee is for Phase A only. Additional fees will be paid for Phase B.
B. APPLICATION OF GAME BOARD DESIGN
The game board design will to be applied to the following game materials:
* Game cards (front and back)
* Sticker for game board tube
* Facilitator's Handbook front and back cover
* Icon for pages inside Facilitator's Handbook
Additional information on the game cards will be provided to the winning designer.
Please note that the project fee is for Phase A only. We will pay additional fees for Phase B, i.e. game cards etc.
NOTE:
Please keep in mind that the game will be used in a corporate setting. The initial target group are Learning and Development (L&D) specialists, mainly people who develop or deliver training courses. They are all educated professionals.
I recently included this feedback in a message to one of the designers:
The game board has to have a level of sophistication and elegance that suits a corporate environment. The game will also be the first direct contact that some potential members will have with the Collegium and has to make a positive impression on them.
We want people to perceive the game as a top-class, creative product.
PLEASE NOTE:
The project fee is now a guaranteed payment.
Target Market(s)
The game will initially be used at networking events held by the Collegium of Skill Advisors in Australia (see: www.csaglobalnet.org). These events are attended by members and guests, with the group ranging from 10 to 20 attendees.
The game may also be used as part of management or leadership development programs in business and government organisations.
Another possible use is with teachers at networking events or professional development courses.
Requirements
Must have
- See the uploaded files for important design requirements.
What is most important is that the game materials are attractive, appealing, impactful. People (in the target group) who see the game materials should feel that they want to find out more, pick up the cards and play the game.
Should not have
- Still thinking....

```html
<!DOCTYPE html>
<html lang="en">
<head>
<meta charset="utf-8">
<title>TRY 45:35:20 — Game Board</title>
<link rel="stylesheet" href="https://fonts.googleapis.com/css2?family=Open+Sans:wght@400;700;800&family=Passion+One:wght@400&display=swap">
<style>
  :root {
    --ink: #111111;
    --paper: #ffffff;
    --navy: #1d3a5f;
    --rule-blue: #1c3e66;
    --corner-red: #ee6b6b;
    --sq-green: #d5e8cb;
    --sq-blue: #d3e9f4;
    --sq-yellow: #f8f3a2;
    --sq-orange: #fbc898;
    --credit-grey: #555555;
  }
  * { box-sizing: border-box; margin: 0; padding: 0; }
  html, body { width: 1200px; height: 848px; overflow: hidden; background: var(--paper); }
  body { font-family: "Open Sans", Arial, sans-serif; color: var(--ink); }

  .canvas {
    position: relative;
    width: 1191px; height: 842px;
    transform: scale(1.0076, 1.0071);
    transform-origin: 0 0;
    border: 3px solid var(--navy);
    background: var(--paper);
  }

  .board-frame { position: absolute; left: 0; top: 0; width: 1191px; height: 842px; }

  .square {
    position: absolute;
    width: 90px; height: 92px;
    border: 2px solid var(--ink);
    display: flex; align-items: center; justify-content: center;
    font-weight: 800; font-size: 21px; line-height: 1.05; text-align: center;
  }
  .square span { display: block; white-space: nowrap; }
  .square--corner { width: 98px; height: 98px; background: var(--corner-red); color: var(--paper); font-size: 22px; }
  .square--green { background: var(--sq-green); }
  .square--blue { background: var(--sq-blue); }
  .square--yellow { background: var(--sq-yellow); }
  .square--orange { background: var(--sq-orange); }

  .row-top .square { top: 28px; height: 97px; }
  .row-bottom .square { top: 668px; height: 97px; }
  .col-left .square { left: 120px; width: 97px; }
  .col-right .square { left: 975px; width: 97px; }

  .row-top .square span { transform: rotate(180deg); }
  .col-left .square span { transform: rotate(90deg); }
  .col-right .square span { transform: rotate(-90deg); }

  .centre-panel {
    position: absolute; left: 230px; top: 138px; width: 735px; height: 517px;
    border: 2px solid var(--ink); background: var(--paper);
  }
  .game-title {
    position: absolute; left: 0; right: 0; top: 62px;
    text-align: center;
    font-family: "Passion One", "Arial Black", sans-serif;
    font-size: 92px; letter-spacing: 1px; color: var(--ink);
    text-shadow: 3px 3px 0 var(--paper), -3px -3px 0 var(--paper), 3px -3px 0 var(--paper), -3px 3px 0 var(--paper), 6px 6px 4px rgba(0,0,0,.35);
  }
  .rules {
    position: absolute; left: 46px; top: 242px; width: 640px; height: 222px;
  }
  .rules svg { position: absolute; inset: 0; }
  .rules-heading {
    position: absolute; left: 0; right: 0; top: 30px; text-align: center;
    font-weight: 700; font-size: 32px;
  }
  .rule { position: absolute; font-weight: 700; font-size: 25px; white-space: nowrap; }
  .rule b { color: var(--rule-blue); font-weight: 700; }
  .panel-credit { position: absolute; top: 493px; font-size: 10.5px; }

  .page-credit {
    position: absolute; top: 790px; font-size: 24px; color: var(--credit-grey);
  }
</style>
</head>
<body>
<main class="canvas">

  <svg class="board-frame" viewBox="0 0 1191 842" aria-hidden="true">
    <path d="M107 12 H1085 V782 H107 Z M121 130 H215 V125 H975 V130 H1071 V664 H975 V668 H215 V664 H121 Z" fill="var(--ink)" fill-rule="evenodd"/>
    <rect x="113" y="18" width="966" height="758" fill="none" stroke="var(--paper)" stroke-width="2"/>
    <rect x="118" y="23" width="956" height="748" fill="var(--paper)"/>
    <rect x="118" y="23" width="956" height="748" fill="none" stroke="var(--ink)" stroke-width="3"/>
  </svg>

  <div class="row-top">
    <div class="square square--corner" style="left:120px"><span style="transform:rotate(135deg)">YIKES!</span></div>
    <div class="square square--green" style="left:232px"><span>20%</span></div>
    <div class="square square--yellow" style="left:338px"><span>ROLL<br>AGAIN</span></div>
    <div class="square square--orange" style="left:444px"><span>70%</span></div>
    <div class="square square--orange" style="left:550px"><span>70%</span></div>
    <div class="square square--orange" style="left:656px"><span>70%</span></div>
    <div class="square square--yellow" style="left:762px"><span>ANY<br>CARD</span></div>
    <div class="square square--blue" style="left:868px"><span>10%</span></div>
    <div class="square square--corner" style="left:975px"><span style="transform:rotate(-135deg)">OOPS!</span></div>
  </div>

  <div class="col-left">
    <div class="square square--green" style="top:138px"><span>20%</span></div>
    <div class="square square--blue" style="top:242px"><span>10%</span></div>
    <div class="square square--yellow" style="top:348px"><span>MISS A<br>TURN</span></div>
    <div class="square square--orange" style="top:455px"><span>70%</span></div>
    <div class="square square--orange" style="top:562px"><span>70%</span></div>
  </div>

  <div class="col-right">
    <div class="square square--green" style="top:138px"><span>20%</span></div>
    <div class="square square--green" style="top:242px"><span>20%</span></div>
    <div class="square square--yellow" style="top:348px"><span>MISS A<br>TURN</span></div>
    <div class="square square--orange" style="top:455px"><span>70%</span></div>
    <div class="square square--orange" style="top:562px"><span>70%</span></div>
  </div>

  <div class="row-bottom">
    <div class="square square--corner" style="left:120px"><span style="transform:rotate(45deg)">UH-OH!</span></div>
    <div class="square square--orange" style="left:232px"><span>70%</span></div>
    <div class="square square--yellow" style="left:338px"><span>ANY<br>CARD</span></div>
    <div class="square square--green" style="left:444px"><span>20%</span></div>
    <div class="square square--green" style="left:550px"><span>20%</span></div>
    <div class="square square--blue" style="left:656px"><span>10%</span></div>
    <div class="square square--yellow" style="left:762px"><span>ROLL<br>AGAIN</span></div>
    <div class="square square--orange" style="left:868px"><span>70%</span></div>
    <div class="square square--corner" style="left:975px"><span style="transform:rotate(-45deg)">CRIKEY!</span></div>
  </div>

  <section class="centre-panel">
    <h1 class="game-title">TRY 45:35:20</h1>

    <div class="rules">
      <svg viewBox="0 0 640 222" aria-hidden="true">
        <path d="M20 3 H620 L637 20 V202 L620 219 H20 L3 202 V20 Z" fill="var(--paper)" stroke="var(--ink)" stroke-width="5"/>
      </svg>
      <h2 class="rules-heading">RULES</h2>
      <p class="rule" style="left:52px;top:102px">10% = <b>3</b></p>
      <p class="rule" style="left:52px;top:150px">20% = <b>6</b></p>
      <p class="rule" style="left:266px;top:120px">70% = <b>9</b></p>
      <p class="rule" style="right:52px;top:102px">Chance = <b>4</b></p>
      <p class="rule" style="right:52px;top:150px">Other = <b>6</b></p>
    </div>

    <p class="panel-credit" style="left:168px">© Dana Holt, Collegium of Skill Advisors</p>
    <p class="panel-credit" style="right:14px">www.csaglobalnet.org</p>
  </section>

  <p class="page-credit" style="left:126px">© Dana Holt, Collegium of Skill Advisors</p>
  <p class="page-credit" style="right:126px">www.csaglobalnet.org</p>

</main>
</body>
</html>
```